Create a promo image to demo to a restaurant the increase in $ they can achieve by using Vesper

Create a promotional image to demonstrate to a restaurant the increase in revenue they can achieve by using Vesper.

We have constructed the attached example of what we are looking for, open to alternatives however the main message is you will make more money from a Vesper event than from your own restaurant for the same guests

We would like the restaurant image to look like the restaurant environment (show other tables in the background) and the same for the Customer dining room (plush private secure)

Please Vesper branding where it fits best

Target Market(s)

Restaurants to signup

Industry/Entity Type

Restaurants and Catering

Requirements
Must have
• Simplicity and obviousness

```html
<!DOCTYPE html>
<html lang="en">
<head>
<meta charset="utf-8">
<title>Vesper Dining – Revenue Comparison</title>
<link href="https://fonts.googleapis.com/css2?family=Heebo:wght@400;500;700;800&display=swap" rel="stylesheet">
<style>
  :root {
    --backdrop: #230a26;
    --plum: #7a2a6e;
    --plum-soft: #8b5083;
    --paper: #ffffff;
    --ink-light: #ffffff;
  }
  * { box-sizing: border-box; margin: 0; padding: 0; }
  html, body { width: 1200px; height: 1200px; overflow: hidden; }
  body { background: var(--backdrop); font-family: "Heebo", Arial, sans-serif; position: relative; }

  .poster { position: absolute; left: 207px; top: 49px; width: 786px; height: 1102px; background: var(--paper); overflow: hidden; }
  .masthead { position: absolute; left: 0; top: 0; width: 786px; height: 128px; background: var(--plum); }
  .brand-dot { position: absolute; left: 178px; top: 26px; width: 150px; height: 150px; border-radius: 50%; background: var(--plum); }
  .brand-name { position: absolute; left: 343px; top: 42px; color: var(--ink-light); font-weight: 700; font-size: 56px; line-height: 1; letter-spacing: -0.5px; }

  .stat { position: absolute; top: 215px; width: 160px; }
  .stat .rule { height: 0; border-top: 2px dashed var(--plum); }
  .stat .icon { width: 80px; height: 48px; margin: 3px auto 3px; background: var(--plum); border-radius: 4px; }
  .stat .card { margin-top: 5px; width: 156px; height: 103px; background: var(--plum); border-radius: 8px; color: var(--ink-light); text-align: center; padding-top: 9px; }
  .stat .headline { font-weight: 800; font-size: 25px; line-height: 1.05; }
  .stat .detail { font-size: 15px; line-height: 19.5px; margin-top: 3px; }

  .table-tab { position: absolute; left: 27px; top: 403px; width: 449px; height: 52px; }
  .table-title { position: absolute; left: 39px; top: 408px; color: var(--plum); font-weight: 700; font-size: 30px; line-height: 1.2; }

  .orders { position: absolute; left: 27px; top: 453px; width: 733px; height: 414px; background: var(--plum); border-radius: 0 4px 4px 4px; color: var(--ink-light); }
  .orders .group { position: absolute; top: 6px; font-weight: 700; font-size: 20px; text-align: center; }
  .orders .vline { position: absolute; border-left: 1.5px dashed rgba(255,255,255,0.85); }
  .row { position: absolute; left: 5px; width: 721px; height: 34px; display: grid; grid-template-columns: 166px 130px 103px 109px 117px 96px; align-items: center; font-size: 18px; }
  .row.shade { background: var(--plum-soft); border-radius: 3px; }
  .row span { text-align: center; }
  .row .item { text-align: left; padding-left: 21px; font-weight: 700; }
  .row.labels { top: 38px; height: 32px; background: var(--paper); color: var(--plum); font-weight: 700; border-radius: 3px; }
  .row.totals { font-weight: 700; font-size: 20px; }

  .perk { position: absolute; top: 891px; width: 185px; height: 182px; border: 1.5px solid var(--plum); background: var(--paper); border-radius: 3px; text-align: center; }
  .perk .cloche { width: 116px; height: 70px; margin: 4px auto 0; background: var(--plum); border-radius: 58px 58px 6px 6px; }
  .perk p { color: var(--plum); font-weight: 500; font-size: 15.5px; line-height: 18px; margin-top: 8px; }
  .band { position: absolute; top: 940px; height: 85px; background: var(--plum); }
  .utensil { position: absolute; top: 900px; width: 26px; height: 162px; border-radius: 13px; background: var(--paper); border: 1.5px solid var(--plum); }
</style>
</head>
<body>
  <main class="poster">
    <header class="masthead">
      <div class="brand-name">Vesper Dining</div>
    </header>
    <div class="brand-dot"></div>

    <section class="stat" style="left:24px">
      <div class="rule"></div>
      <div class="icon" role="img" aria-label="Icon of coin stacks with a rising arrow"></div>
      <div class="rule"></div>
      <div class="card"><div class="headline">326%</div><div class="detail">more income<br>by looking outside<br>your 4 walls</div></div>
    </section>
    <section class="stat" style="left:216px">
      <div class="rule"></div>
      <div class="icon" role="img" aria-label="Icon of an umbrella deflecting arrows"></div>
      <div class="rule"></div>
      <div class="card"><div class="headline">People</div><div class="detail">who hold<br>Vespers<br>are recession proof</div></div>
    </section>
    <section class="stat" style="left:410px">
      <div class="rule"></div>
      <div class="icon" role="img" aria-label="Icon of a dollar sign over a rising bar chart"></div>
      <div class="rule"></div>
      <div class="card"><div class="headline">Immediatley</div><div class="detail">improve<br>your<br>cash flow</div></div>
    </section>
    <section class="stat" style="left:602px">
      <div class="rule"></div>
      <div class="icon" role="img" aria-label="Icon of a pointing hand tapping"></div>
      <div class="rule"></div>
      <div class="card"><div class="headline">Vesper</div><div class="detail">is the<br>answer</div></div>
    </section>

    <svg class="table-tab" viewBox="0 0 449 52" aria-hidden="true">
      <path d="M1.5 52 V1.5 H412 Q418 1.5 422 8 L447 52" fill="none" stroke="#7a2a6e" stroke-width="3"/>
    </svg>
    <h2 class="table-title">Typical Ordering for 8 covers:</h2>

    <section class="orders">
      <div class="group" style="left:301px;width:212px">In House Ordering</div>
      <div class="group" style="left:513px;width:220px">Vesper Ordering</div>
      <div class="vline" style="left:301px;top:0;height:377px"></div>
      <div class="vline" style="left:513px;top:0;height:377px"></div>
      <div class="vline" style="left:171px;top:72px;height:305px"></div>
      <div class="vline" style="left:404px;top:38px;height:339px"></div>
      <div class="vline" style="left:631px;top:38px;height:339px"></div>

      <div class="row labels"><span></span><span>Sell Price</span><span>Take up</span><span>Spend</span><span>Take up</span><span>Spend</span></div>
      <div class="row" style="top:72px"><span class="item">Canapes</span><span>8</span><span></span><span>0</span><span>16</span><span>128</span></div>
      <div class="row shade" style="top:110px"><span class="item">Entrée</span><span>25</span><span>4</span><span>100</span><span>8</span><span>200</span></div>
      <div class="row" style="top:148px"><span class="item">Mains</span><span>45</span><span>6</span><span>270</span><span>8</span><span>360</span></div>
      <div class="row shade" style="top:187px"><span class="item">Entrée as Main</span><span>25</span><span>2</span><span>50</span><span></span><span>0</span></div>
      <div class="row" style="top:225px"><span class="item">Desserts</span><span>25</span><span>2</span><span>50</span><span>8</span><span>200</span></div>
      <div class="row shade" style="top:264px"><span class="item">Sides</span><span>12</span><span>1</span><span>12</span><span>4</span><span>48</span></div>
      <div class="row" style="top:302px"><span class="item">Cocktails</span><span>25</span><span>2</span><span>50</span><span>8</span><span>200</span></div>
      <div class="row shade" style="top:341px"><span class="item">Staff</span><span>300</span><span></span><span></span><span>2</span><span>600</span></div>
      <div class="vline" style="left:5px;width:721px;top:377px;height:0;border-left:none;border-top:1.5px dashed rgba(255,255,255,0.85)"></div>
      <div class="row totals" style="top:381px"><span></span><span></span><span></span><span>532</span><span></span><span>1736</span></div>
    </section>

    <div class="band" style="left:213px;width:81px"></div>
    <div class="band" style="left:486px;width:81px"></div>
    <div class="utensil" style="left:240px" role="img" aria-label="Spoon"></div>
    <div class="utensil" style="left:514px" role="img" aria-label="Fork"></div>

    <section class="perk" style="left:28px">
      <div class="cloche" role="img" aria-label="Serving cloche with a money bag"></div>
      <p>Achieve 3+ times<br>the spend<br>for the same<br>number</p>
    </section>
    <section class="perk" style="left:300px">
      <div class="cloche" role="img" aria-label="Serving cloche with staff and dollar coins"></div>
      <p>Cover your staff<br>cost over and<br>above your<br>menu spend</p>
    </section>
    <section class="perk" style="left:573px">
      <div class="cloche" role="img" aria-label="Serving cloche with a dining table"></div>
      <p>Vespers are an occasion<br>and everyone has<br>everything,<br>cocktails, sides<br>and canapes</p>
    </section>
  </main>
</body>
</html>
```